Web Design Project

We are looking for a unified design of Corporate Website, Stationary (Including Letterhead and Envelopes), Business Cards, Email Footers and Sales & Marketing Brochures.

Color palette should include:
Black (R: 24, G:24, B:24)
Red (R:206, G:0, B:39)
Dark Grey (R:51, G:51, B:51)
Light Grey/Silver (R:203, G:203, B:203)

As we do business in North America and the UK, designs should be reflective of standard sizing for both regions.

Check out our website to better understand who we are: www.KLVT.com and a copy of our Logo has been uploaded for reference.
Updates

Hello all, we had not anticipated the volume of unique, high quality designs we have received, thank you all for your submissions. A team review of all designs will take place the week of December 8th, and final decisions and selections made. Thank you again

Target Market(s)

Automotive Parts Wholesalers, Vehicle Repair Specialists, Automotive Parts Manufacturers, Automotive Insurance

Industry/Entity Type

Business

Font styles to use
Sans Serif

Requirements
Must have
• - Color palette should include:
- Black (R: 24, G:24, B:24)
- Red (R:206, G:0, B:39)
- Dark Grey (R:51, G:51, B:51)
- Light Grey/Silver (R:203, G:203, B:203)
Should not have
• No Animations

```html
<!DOCTYPE html>
<html lang="en">
<head>
<meta charset="utf-8">
<title>Kelvant Parts Solutions</title>
<link href="https://fonts.googleapis.com/css2?family=Open+Sans:wght@400;600;700&family=Roboto+Condensed:wght@400;700&display=swap" rel="stylesheet">
<style>
:root{
  --black:#181818;
  --red:#ce0027;
  --dark:#333333;
  --silver:#cbcbcb;
  --text:#555;
  --muted:#999;
  --white:#fff;
}
*{margin:0;padding:0;box-sizing:border-box}
html,body{width:1200px;height:2230px;overflow:hidden;background:var(--white);font-family:"Open Sans",Arial,sans-serif;color:var(--text)}
.page{position:relative;width:1200px;height:2230px}
.abs{position:absolute}

.hero{left:0;top:0;width:1200px;height:779px;background:radial-gradient(ellipse at 55% 55%,#8a8a8a 0%,#5a5a5a 35%,#2e2e2e 75%,#1f1f1f 100%)}
.brand{left:100px;top:30px;display:flex;align-items:center;gap:12px;color:#ddd;font-weight:700;font-size:30px;letter-spacing:1px;line-height:1}
.brand .mark{width:50px;height:50px;border:4px solid #bbb;border-radius:50%}
.brand small{display:block;font-size:15px;font-weight:600;letter-spacing:3px;color:#bbb;margin-top:2px}
.call{left:550px;top:32px;color:#ccc;font-size:17px;line-height:22px}
.call svg{position:absolute;left:148px;top:8px}
.lang{left:898px;top:20px;font-size:12px;color:#ddd}
.lang i{display:inline-block;width:16px;height:10px;background:var(--red);margin-left:6px;vertical-align:middle}
.login{left:1063px;top:20px;font-size:13px;color:#ddd}
.search{left:860px;top:54px;width:241px;height:34px;background:#e6e6e6;border:1px solid #999}
.search b{position:absolute;right:0;top:0;width:32px;height:32px;background:var(--black)}
.nav{left:101px;top:111px;width:999px;height:46px;display:flex;background:linear-gradient(#d8d8d8,#a9a9a9);box-shadow:0 6px 14px rgba(0,0,0,.5)}
.nav a{display:flex;align-items:center;justify-content:center;font-size:12.5px;color:#222;text-decoration:none;border-right:1px solid #888;padding:0 20px;height:100%}
.nav a.active{background:var(--black);color:#fff;width:107px}
.arrow{top:386px;width:36px;height:36px;border-radius:50%;background:rgba(160,160,160,.6)}
.caption{left:101px;top:711px;width:999px;height:68px;background:linear-gradient(#3c3c3c,#1c1c1c);color:#ddd;font-size:19px;font-weight:600;display:flex;align-items:center;justify-content:center}

.welcome{left:100px;top:826px;width:1000px;text-align:center}
.welcome h1{font-weight:400;font-size:26px;color:#222;margin-bottom:14px}
.welcome p{font-size:13.4px;line-height:18px;color:#777}
.btn-red{display:inline-block;background:var(--red);color:#fff;font-size:14px;padding:6px 22px;margin-top:24px;box-shadow:0 2px 0 #8a0019}

.feature{top:1030px;width:300px;text-align:center;color:#222}
.feature h3{font-weight:400;font-size:19px;line-height:22px;margin:14px 0 16px}
.feature p{font-size:14px;line-height:18px}

.video{left:100px;top:1279px;width:1000px;height:89px;background:linear-gradient(#d8002b,#c20025);border-radius:3px;color:#fff;display:flex;align-items:center;font-size:19px;font-weight:600}
.video span{margin-left:150px}
.video b{margin-left:54px;width:210px;height:36px;background:#fff;color:#222;font-weight:400;font-size:16px;display:flex;align-items:center;justify-content:center;border-radius:2px}

.post{top:1424px;width:228px;font-family:Arial,sans-serif}
.post .photo{height:137px}
.post h4{font-size:10px;color:#333;margin-top:21px}
.post em{display:block;font-size:8px;color:#999;margin-top:3px}
.post p{font-size:10px;line-height:13px;color:#aaa;margin-top:8px}
.post .more{display:inline-block;background:#888;color:#fff;font-size:9.5px;font-weight:700;padding:3px 7px;margin-top:10px}
.post .more.dark{background:#3a0a0a}

.partners{left:97px;top:1752px;width:1003px;display:flex;gap:60px;overflow:hidden;white-space:nowrap;font-size:29px;color:#888;font-weight:600;align-items:center}
.partners span{display:flex;align-items:center;gap:8px}
.partners i{display:inline-block;width:30px;height:30px;background:#999;border-radius:50%}
.partners i.sq{border-radius:3px}

.footer{left:0;top:1871px;width:1200px;height:300px;background:#2f2f2f;color:#999;font-size:12px}
.footer h5{font-family:"Roboto Condensed",Arial,sans-serif;font-weight:400;color:#fff;font-size:20px;margin-bottom:16px}
.fcol{position:absolute;top:32px}
.fcol p{line-height:18px}
.blog strong{display:block;color:#fff;font-size:12px;font-weight:600}
.blog p{margin-bottom:12px}
.menu p{font-size:11px;line-height:18px;text-transform:uppercase}
.social{display:flex;gap:14px;margin-top:6px}
.social i{width:11px;height:11px;background:#fff;border-radius:2px}
.field{width:232px;background:#fff;border:1px solid #ccc;color:#999;font-size:10px;padding:8px 16px;margin-bottom:10px}
.send{margin-left:112px;display:inline-block;background:var(--red);color:#fff;font-size:10.5px;padding:7px 16px}
.bottom{left:0;top:2171px;width:1200px;height:59px;background:var(--black);color:#fff;font-size:13px;display:flex;align-items:center;justify-content:center}
.bottom small{position:absolute;right:18px;font-size:12px}
</style>
</head>
<body>
<div class="page">

  <header class="abs hero" role="img" aria-label="Photo of assorted automotive parts: brake disc, shock absorber, filters and pulleys on a grey backdrop"></header>

  <div class="abs brand"><span class="mark"></span><div>KELVANT<small>parts solutions</small></div></div>
  <div class="abs call">Question?<br>Call us 55501234
    <svg width="26" height="26" viewBox="0 0 26 26"><circle cx="13" cy="13" r="11" fill="none" stroke="#aaa" stroke-width="2"/><path d="M9 8c1 4 4 8 8 9l1-2-3-1-1 1c-1-1-2-2-3-4l1-1-1-3z" fill="#aaa"/></svg>
  </div>
  <div class="abs lang">Language: <i></i> ▾</div>
  <div class="abs login">Login</div>
  <div class="abs search"><b><svg width="32" height="32" viewBox="0 0 32 32"><circle cx="15" cy="15" r="5" fill="none" stroke="#fff" stroke-width="2"/><path d="M19 19l4 4" stroke="#fff" stroke-width="2"/></svg></b></div>

  <nav class="abs nav">
    <a class="active">HOME</a>
    <a>INTELLIGENT SALES &amp; MARKETING</a>
    <a>KELVANT AWARDS</a>
    <a>REFERENCES</a>
    <a>ABOUT US</a>
    <a>CAREERS</a>
    <a style="border:0">CONTACT US</a>
  </nav>

  <div class="abs arrow" style="left:24px"><svg width="36" height="36"><path d="M21 11l-7 7 7 7" fill="none" stroke="#333" stroke-width="3"/></svg></div>
  <div class="abs arrow" style="left:1139px"><svg width="36" height="36"><path d="M15 11l7 7-7 7" fill="none" stroke="#333" stroke-width="3"/></svg></div>

  <div class="abs caption">We are Automotive Parts Wholesalers, Vehicle Repair Specialists, Automotive Parts Manufacturers</div>

  <section class="abs welcome">
    <h1>Welcome To Our Site</h1>
    <p>Pellentesque sem metus, tempus non blandit non, varius et tellus. Etiam volutpat sem ut iaculis tempus. Vivamus mi ex, auctor sit amet vehicula non, hendrerit nec urna. Donec purus quam, porta eget quam in, convallis viverra dui. Pellentesque libero sem, commodo a ipsum eget, rutrum ullamcorper tellus. Donec accumsan efficitur vehicula. Praesent arcu enim, dictum ac nibh sit amet, auctor rutrum mauris. In tempor diam sed lorem consequat.</p>
    <span class="btn-red">Read More</span>
  </section>

  <div class="abs feature" style="left:106px">
    <svg width="52" height="52" viewBox="0 0 52 52"><circle cx="26" cy="16" r="12" fill="none" stroke="#111" stroke-width="3"/><path d="M14 16h24M26 4v24" stroke="#111" stroke-width="2"/><circle cx="12" cy="34" r="5" fill="#111"/><circle cx="40" cy="34" r="5" fill="#111"/><path d="M2 50c0-8 4-11 10-11s10 3 10 11zM30 50c0-8 4-11 10-11s10 3 10 11z" fill="#111"/></svg>
    <h3>Automotive Parts<br>Wholesalers</h3>
    <p>Lorem ipsum dolor sit amet, consectetur adipiscing elit. Pellentesque at arcu urna. Class aptent</p>
  </div>
  <div class="abs feature" style="left:445px">
    <svg width="70" height="52" viewBox="0 0 70 52"><circle cx="14" cy="8" r="6" fill="#111"/><path d="M6 16h16v20h-4v16h-8V36H6z" fill="#111"/><path d="M32 38l5-10h20l5 10v10H32z" fill="#111"/><circle cx="38" cy="48" r="3" fill="#fff"/><circle cx="56" cy="48" r="3" fill="#fff"/></svg>
    <h3>Vehicle Repair<br>Specialists</h3>
    <p>Lorem ipsum dolor sit amet, consectetur adipiscing elit. Pellentesque at arcu urna. Class aptent</p>
  </div>
  <div class="abs feature" style="left:799px">
    <svg width="52" height="52" viewBox="0 0 52 52"><circle cx="26" cy="26" r="18" fill="none" stroke="#111" stroke-width="8" stroke-dasharray="7 7"/><circle cx="26" cy="26" r="14" fill="#111"/><circle cx="26" cy="26" r="6" fill="#fff"/></svg>
    <h3>Automotive Parts<br>Manufacturers</h3>
    <p>Lorem ipsum dolor sit amet, consectetur adipiscing elit. Pellentesque at arcu urna. Class aptent</p>
  </div>

  <div class="abs video"><span>CLICK HERE TO WATCH OUR CORPORATE VIDEO</span><b>Watch Now</b></div>

  <article class="abs post" style="left:101px">
    <div class="photo" role="img" aria-label="Car body assembly line with yellow robotic frames" style="background:linear-gradient(135deg,#9a9a7a,#c9b84a 50%,#6d6d6d)"></div>
    <h4>Preparing dish for you with love</h4><em>22 Sept 2013, by Admin</em>
    <p>Etiam pretium quam sed lectus mollis, sed cursus. Phasellus vitae mollis sem.</p>
    <span class="more dark">Read More</span>
  </article>
  <article class="abs post" style="left:357px">
    <div class="photo" role="img" aria-label="Mechanic in blue cap working under a car bonnet" style="background:linear-gradient(135deg,#d8d4cc,#7d8ea8 55%,#3a4c78)"></div>
    <h4>Customization is as easy as playing</h4><em>22 Sept 2013, by Admin</em>
    <p>Etiam pretium quam sed lectus mollis, sed element</p>
    <span class="more">Read More</span>
  </article>
  <article class="abs post" style="left:614px">
    <div class="photo" role="img" aria-label="Hands with a wrench repairing an engine" style="background:linear-gradient(135deg,#3a3a3a,#8a5a4a 50%,#2a2a2a)"></div>
    <h4>Preparing dish for you with love</h4><em>22 Sept 2013, by Admin</em>
    <p>Etiam pretium quam sed lectus mollis, sed cursus. Phasellus vitae mollis sem.</p>
    <span class="more">Read More</span>
  </article>
  <article class="abs post" style="left:871px">
    <div class="photo" role="img" aria-label="Workers in a car factory hall" style="background:linear-gradient(135deg,#b8c0c8,#8a8e94 50%,#5a5052)"></div>
    <h4>Customization is as easy as playing</h4><em>22 Sept 2013, by Admin</em>
    <p>Etiam pretium quam sed lectus mollis, sed element</p>
    <span class="more">Read More</span>
  </article>

  <div class="abs partners">
    <span><i></i>Tunewave</span>
    <span><i class="sq"></i>Gridsoft</span>
    <span>Snapframe</span>
    <span>Stockpix</span>
    <span><i class="sq"></i>Tilepay</span>
    <span>Dreamco</span>
  </div>

  <footer class="abs footer">
    <div class="fcol" style="left:103px">
      <h5>CONTACT</h5>
      <p>T:800.555.0142<br>M: 604.555.0187<br>E: info@kelvantds.com</p>
      <p style="margin-top:18px">Kelvant DataSystems Corporation<br>Suite 210 - 4400 Harbour Way<br>Northgate, British Columbia,<br>Canada V0X 2Y4</p>
      <h5 style="margin:10px 0 14px">LETS CONNECT</h5>
      <div class="social"><i></i><i></i><i></i><i></i></div>
    </div>
    <div class="fcol blog" style="left:381px;width:240px">
      <h5>BLOG POSTS</h5>
      <strong>Lorem ipsum dolor sit</strong><p>Lorem ipsum dolor sit amet, consectetur adipiscing elit. Donec sed auctor elit.</p>
      <strong>Contantry popilar sit amit</strong><p>Lorem ipsum dolor sit amet, consectetur adipiscing elit. Donec sed auctor elit.</p>
      <strong>Ipsum sil tlosrm ipsum dolor</strong><p>Lorem ipsum dolor sit amet, consectetur adipiscing elit. Donec sed auctor elit.</p>
    </div>
    <div class="fcol menu" style="left:694px;width:130px">
      <h5>MENU</h5>
      <p>Home<br>Intelligent Sales &amp;<br>Marketing<br>Kelvant Awards<br>References<br>About Us<br>Careers<br>Contact Us</p>
    </div>
    <div class="fcol" style="left:871px">
      <h5>CONTACT US</h5>
      <div class="field">YOUR E-MAIL...</div>
      <div class="field" style="height:72px">YOUR TEXT...</div>
      <span class="send">SEND MESSAGE</span>
    </div>
  </footer>

  <div class="abs bottom">Copyright © yourwebsite &nbsp;|&nbsp; Terms &amp; Conditions<small>M3</small></div>
</div>
</body>
</html>
```